Atelier Vane Architecture business card

We need to update our business card. We do high end custom residential, hospitality, and wellness architecture. We focus on creating unique spaces and design around the five senses, believing that architecture's true impact is not on our surroundings, but within us. We would like to see designs are instill a sense of calm awe. They should be crisp, fresh, clean, authentic, & contemporary without being sterile, overworked, or harsh. White space is important. Alternative materials are an option if natural. We have created our own logo and would like designs to incorporate it. However, we are willing to see alternatives if the logo becomes a stumbling block and you have an alternate you suggest. Card must have the following information:
Atelier Vane Architecture, Inc.
742 Marbury Rd. NE Atlanta, GA 30319
Dominic K. Whitlow, AIA, NCARB, LEED AP BD+C
ateliervane.example

Target Market(s)

Higher net worth individuals with an appreciation for design, nature, sustainability,

Industry/Entity Type

Architect

Contact Information for Business Card

See above. The title of Owner or Architect is helpful but not necessary. Minimalism should trump additional information.

Font styles to use
Serif
Sans Serif

Requirements
Must have
• It should look professional. It must use logo
Should not have
• caligraphy, animals, anything that is cute,

```html
<!DOCTYPE html>
<html lang="en">
<head>
<meta charset="utf-8">
<title>Atelier Vane Architecture — Business Card</title>
<link rel="stylesheet" href="https://fonts.googleapis.com/css2?family=Roboto:wght@400;500&family=Tinos&display=swap">
<style>
  :root {
    --backdrop: #d9d9d7;
    --card: #f6f6f4;
    --ink: #2b2b2b;
    --ink-soft: #6f6f6f;
    --accent-green: #1e7a3c;
    --card-shadow: 0 6px 18px rgba(0,0,0,0.16);
  }
  * { margin: 0; padding: 0; box-sizing: border-box; }
  html, body {
    width: 1200px; height: 900px; overflow: hidden;
    background: var(--backdrop);
  }
  .canvas {
    position: relative; width: 1200px; height: 900px;
  }
  .card {
    position: absolute;
    width: 620px; height: 354px;
    background: var(--card);
    box-shadow: var(--card-shadow);
  }
  /* Brand side */
  .card--brand { left: 290px; top: 56px; }
  .brand-name {
    position: absolute; left: 0; right: 0; top: 118px;
    text-align: center;
    font-family: "Tinos", serif;
    font-size: 34px; letter-spacing: 0.14em;
    color: var(--ink);
  }
  .brand-rule {
    position: absolute; left: 130px; right: 130px; top: 172px;
    height: 1px; background: var(--ink-soft);
  }
  .tagline {
    position: absolute; left: 0; right: 0; top: 206px;
    text-align: center;
    font-family: "Tinos", serif;
    font-size: 15px; color: var(--ink);
  }
  /* Contact side */
  .card--contact { left: 290px; top: 490px; }
  .person {
    position: absolute; left: 40px; top: 38px;
    padding-left: 14px;
    border-left: 4px solid var(--accent-green);
    font-family: "Roboto", sans-serif;
  }
  .person__name { font-size: 21px; font-weight: 500; color: var(--ink); line-height: 1.1; }
  .person__credentials { font-size: 11px; color: var(--ink-soft); margin-top: 4px; letter-spacing: 0.02em; }
  .card-logo {
    position: absolute; right: 40px; top: 150px;
    font-family: "Roboto", sans-serif;
    font-size: 17px; font-weight: 400; letter-spacing: 0.12em;
    color: var(--ink);
    text-transform: uppercase;
  }
  .contact-list {
    position: absolute; left: 40px; bottom: 36px;
    list-style: none;
    font-family: "Roboto", sans-serif;
    font-size: 14px; color: var(--ink);
  }
  .contact-list li { display: flex; align-items: center; gap: 8px; line-height: 22px; }
  .contact-list svg { width: 12px; height: 12px; fill: var(--ink-soft); flex: none; }
</style>
</head>
<body>
<main class="canvas">

  <section class="card card--brand" aria-label="Card front">
    <div class="brand-name">Atelier Vane Architecture</div>
    <div class="brand-rule"></div>
    <p class="tagline">High end custom residential, hospitality, and wellness architecture</p>
  </section>

  <section class="card card--contact" aria-label="Card back">
    <div class="person">
      <div class="person__name">Dominic K. Whitlow</div>
      <div class="person__credentials">AIA, NCARB, LEED AP BD+C</div>
    </div>

    <div class="card-logo">Atelier Vane Architecture</div>

    <ul class="contact-list">
      <li>
        <svg viewBox="0 0 12 12" aria-hidden="true"><path d="M6 0a4 4 0 0 0-4 4c0 3 4 8 4 8s4-5 4-8a4 4 0 0 0-4-4zm0 5.5A1.5 1.5 0 1 1 6 2.5a1.5 1.5 0 0 1 0 3z"/></svg>
        742 Marbury Rd. NE Atlanta, GA 30319
      </li>
      <li>
        <svg viewBox="0 0 12 12" aria-hidden="true"><path d="M2.5 0.5l2 2-1 1.5c.7 1.6 2 2.9 3.5 3.5l1.5-1 2 2-1.2 2C5 10.3 1.7 7 0.5 1.7z"/></svg>
        0934-5120-7786
      </li>
      <li>
        <svg viewBox="0 0 12 12" aria-hidden="true"><path d="M0 2h12v8H0zM1 3l5 3.5L11 3v-.2H1z" fill-rule="evenodd"/></svg>
        dominic@ateliervane.example
      </li>
      <li>
        <svg viewBox="0 0 12 12" aria-hidden="true"><path d="M0 1h12v8H0zM1 2v6h10V2zM3 10h6v1H3z" fill-rule="evenodd"/></svg>
        www.ateliervane.example
      </li>
    </ul>
  </section>

</main>
</body>
</html>
```